App UI Design: Shopping/E-commerce App

Project :
Develop an UI design & App icon for an E-commerce/Shopping App

About the App/ Target Audience:
This grocery & food shopping app will be used by independent pub, café, restaurant owners to place & manage their purchases of foods and groceries for their catering businesses.

They will use the app to access product catalogues & special promotions, search & buy large quantities of groceries or catering supplies, and the ability to manage and track status of their order.

The HTML5 App’s has been built with a very basic structure. It now needs the visual layer of the UI designed

Note:
The app is tailored for business & catering orders, not retail/supermarket buyers, so the visual needs to look smart & not too casual.

Reason: Current submissions have not met out expectations. Please use the similar app examples in the PDF as a strong point of reference for the look & feel. Feedback will be given as submissions come in, please feel free to submit initial concepts of 1 or 2 of the pages & we'll provide feedback on whether it is on the right track or not before you do more work. Current submission will also receive feedback in the next few days. We look forward to new submissions!

Target Market(s)

Male & Female. Independent pub, café, restaurant owners buying for their catering businesses. Chefs etc.

Industry/Entity Type

Restaurant

Requirements
Must have
• An overview of elements/pages of the app that needs to be designed are:
(DOWNLOAD a more detailed diagram PDF explanation)

1. Welcome- Log-in Page
2. Homepage – index that links to different function of the app

Products:
3. Promotions page – for products on special for a limited time
4. Catalogue page – access to a range of catalogue

Ways to buy:
5. Basket (Shopping Cart) - tracking items they are buying from the catalogues
6. Templates (Pre-set Shopping list)- Set shopping list that has been preloaded for certain menu
7. Open Order page

My Account:
8. My Account/profile page – Users can check the status of their order, look at past orders, look at their account number & details etc

_______________________________________________________

Icon set- Icons to represent each pages that act as visual cues for easier browsing.

2 Main features that need to be accessible & consistent throughout all pages are:
a) The Navigation Bar –
so the user can quickly find their way back & access to the main functions
b) The Search bar –
whether it drops down when needed, or is featured as a header/footer.
c) Log out button
Nice to have
• _______________________________________________________

Things to keep in mind:

The UI design essentially needs to be a customizable template that can easily adapt to any brand/logo with a slight change of the color scheme. As we will later implement our brand & logo onto it.

We’re looking for a clean & clear design that allows for a straight forward easy user experience.

You are free to develop different layout & UI pattern that you feel is the most efficient way the user can walk through the App & make their purchase in no more than 2 or 3 clicks
________________________________________________

Screenshot of Similar Apps for reference are also in the PDF

```html
<!DOCTYPE html>
<html lang="en">
<head>
<meta charset="utf-8">
<title>eShopping – Catering Supplies App Screens</title>
<link href="https://fonts.googleapis.com/css2?family=Arimo:wght@400;700&display=swap" rel="stylesheet">
<style>
  :root{
    --page-bg:#e6e7e9;
    --status-bg:#0c0c0c;
    --blue-top:#62b0ee;
    --blue-bottom:#3b8fd8;
    --blue-btn:#2f86d6;
    --blue-text:#3d95dd;
    --white:#ffffff;
    --screen-light:#f1f1f1;
    --text-dark:#333333;
    --text-mid:#555555;
    --text-soft:#9a9a9a;
    --line:#d6d6d6;
    --tile-dark:#3a3a3a;
    --tile-edge:#262626;
    --icon-light:#dedede;
    --photo-a:#d9c6ad;
    --photo-b:#6e5140;
    --photo-c:#f2ece3;
  }
  *{box-sizing:border-box;margin:0;padding:0}
  html,body{width:1200px;height:709px;overflow:hidden}
  body{background:var(--page-bg);font-family:"Arimo",Arial,sans-serif;color:var(--text-dark);position:relative}
  .screen{position:absolute;top:90px;width:378px;height:573px;transform:scale(.923);transform-origin:0 0;overflow:hidden;box-shadow:0 6px 22px rgba(0,0,0,.18)}
  .screen--promotions{left:38px;background:var(--white)}
  .screen--login{left:425px;background:var(--screen-light)}
  .screen--home{left:813px;background:var(--white)}

  .status-bar{height:27px;background:var(--status-bg);color:var(--white);display:flex;align-items:center;justify-content:space-between;padding:0 8px;font-size:15px;font-weight:700}
  .status-bar svg{display:block}

  .app-header{height:53px;background:linear-gradient(var(--blue-top),var(--blue-bottom));display:flex;align-items:center;justify-content:space-between;padding:0 6px;border-bottom:1px solid #2f7fc4}
  .header-btn{width:54px;height:42px;background:var(--blue-btn);border-radius:2px;display:flex;align-items:center;justify-content:center;box-shadow:inset 0 1px 0 rgba(255,255,255,.15)}
  .header-title{color:var(--white);font-size:22px;font-weight:700;text-shadow:0 1px 1px rgba(0,0,0,.2)}

  .product-head{height:60px;display:flex;align-items:center;justify-content:space-between;padding:0 16px;border-bottom:1px solid var(--line);font-size:14.5px;font-weight:700;color:var(--text-dark)}
  .product-price{font-weight:700;color:var(--text-mid);font-size:16px}
  .product-photo{position:relative;height:248px;background:radial-gradient(ellipse at 45% 45%,var(--photo-c) 0%,var(--photo-a) 40%,var(--photo-b) 100%)}
  .product-caption{position:absolute;left:0;right:0;bottom:0;height:64px;background:rgba(20,20,20,.82);color:var(--white);font-size:11px;line-height:13px;padding:11px 16px 0}

  .offer-row{height:62px;display:flex;align-items:center;justify-content:space-between;padding:0 6px 0 18px;border-bottom:1px solid var(--line);background:linear-gradient(#ffffff,#f3f3f3)}
  .offer-name{font-size:14px;font-weight:700;color:var(--text-dark)}
  .offer-qty{font-size:12px;color:var(--text-dark);margin-top:1px}
  .basket-btn{width:130px;height:36px;background:linear-gradient(var(--blue-top),var(--blue-bottom));border-radius:3px;color:var(--white);font-size:13.5px;display:flex;align-items:center;justify-content:center;gap:8px}

  .tab-bar{position:absolute;left:0;right:0;bottom:0;height:58px;background:linear-gradient(#3d3d3d,#262626);display:flex}
  .tab{flex:1;display:flex;align-items:center;justify-content:center;border-right:1px solid #1b1b1b;border-left:1px solid #4a4a4a}
  .tab--active{background:linear-gradient(var(--blue-top),var(--blue-bottom))}

  .logo-badge{width:76px;height:76px;border-radius:50%;background:radial-gradient(circle at 50% 35%,#ffffff,#e4e4e4);box-shadow:0 1px 3px rgba(0,0,0,.25);display:flex;align-items:center;justify-content:center;color:var(--blue-text);font-size:10px;font-weight:700;letter-spacing:.5px;position:absolute;left:152px;top:115px}

  .login-form{position:absolute;left:44px;top:277px;width:292px}
  .field-group{background:var(--white);border:1px solid #cfcfcf;border-radius:3px}
  .field{height:42px;display:flex;align-items:center;justify-content:space-between;padding:0 10px 0 13px;font-size:13px}
  .field + .field{border-top:1px solid #e2e2e2}
  .field--filled{color:var(--text-dark)}
  .field--empty{color:#b3b3b3}
  .caret{display:inline-block;width:1px;height:13px;background:var(--blue-text);vertical-align:-2px;margin-left:1px}
  .signin-btn{margin-top:15px;height:49px;border-radius:3px;background:linear-gradient(var(--blue-top),var(--blue-bottom));color:var(--white);font-size:17px;font-weight:700;display:flex;align-items:center;justify-content:center}
  .forgot-link{margin-top:12px;text-align:center;font-size:11px;font-weight:700;color:var(--text-dark)}

  .welcome{position:relative;height:252px;border-bottom:1px solid var(--line)}
  .welcome .logo-badge{top:35px}
  .welcome-name{position:absolute;top:133px;left:0;right:0;text-align:center;color:var(--blue-text);font-size:16px;font-weight:700}
  .welcome-text{position:absolute;top:160px;left:40px;right:40px;text-align:center;font-size:10.5px;line-height:15px;color:var(--text-dark)}

  .menu-grid{display:grid;grid-template-columns:repeat(3,1fr);grid-template-rows:repeat(2,120px);height:241px;background:var(--tile-edge);gap:1px}
  .menu-tile{background:var(--tile-dark);display:flex;flex-direction:column;align-items:center;justify-content:flex-end;padding-bottom:12px;color:var(--white);font-size:10px;font-weight:700;letter-spacing:.2px}
  .menu-tile svg{margin-bottom:14px}
  .menu-tile--active{background:linear-gradient(#3c9af0,#2d85d4)}
</style>
</head>
<body>

<svg width="0" height="0" style="position:absolute" aria-hidden="true">
  <defs>
    <symbol id="icon-promotions" viewBox="0 0 32 32">
      <rect x="5" y="4" width="22" height="17" fill="currentColor"/>
      <rect x="14.5" y="1.5" width="3" height="3" fill="currentColor"/>
      <path d="M16 21v9M16 21l-7 9M16 21l7 9" stroke="currentColor" stroke-width="1.8" fill="none"/>
      <path d="M16 7l1.4 3 3.2.3-2.4 2.1.8 3.1L16 13.9l-3 1.6.8-3.1-2.4-2.1 3.2-.3z" fill="#333"/>
      <path d="M10.5 14l.8 1.5 1.6.2-1.2 1 .4 1.6-1.6-.8-1.5.8.3-1.6-1.2-1 1.7-.2z" fill="#333"/>
      <path d="M21.5 14l.8 1.5 1.6.2-1.2 1 .4 1.6-1.6-.8-1.5.8.3-1.6-1.2-1 1.7-.2z" fill="#333"/>
    </symbol>
    <symbol id="icon-catalogue" viewBox="0 0 32 32">
      <path d="M6 2h15l6 6v22H6z" fill="currentColor"/>
      <path d="M21 2v6h6" fill="#999"/>
      <path d="M9.5 9h9M9.5 13h13M9.5 16h13M9.5 19h13M9.5 22h13M9.5 25h9" stroke="#444" stroke-width="1.2"/>
    </symbol>
    <symbol id="icon-basket" viewBox="0 0 32 32">
      <path d="M9 13a7 7 0 0 1 14 0" stroke="currentColor" stroke-width="2.2" fill="none"/>
      <rect x="2" y="12" width="28" height="4" rx="1" fill="currentColor"/>
      <path d="M4 17h24l-2.5 12h-19z" fill="currentColor"/>
      <path d="M10 19.5v7M16 19.5v7M22 19.5v7" stroke="#3a3a3a" stroke-width="2.6" stroke-linecap="round"/>
    </symbol>
    <symbol id="icon-template" viewBox="0 0 32 32">
      <rect x="5" y="4" width="22" height="27" rx="1.5" fill="currentColor"/>
      <rect x="11" y="1" width="10" height="6" rx="1.5" fill="currentColor" stroke="#444" stroke-width="1"/>
      <path d="M9 12h1.6M9 16h1.6M9 20h1.6M9 24h1.6" stroke="#444" stroke-width="1.6"/>
      <path d="M13 12h10M13 16h10M13 20h10M13 24h10" stroke="#444" stroke-width="1.2"/>
    </symbol>
    <symbol id="icon-open-order" viewBox="0 0 32 32">
      <path d="M3 5h4l5 19h16" stroke="currentColor" stroke-width="2" fill="none"/>
      <circle cx="13" cy="27.5" r="2.3" fill="currentColor"/>
      <rect x="11" y="7" width="15" height="13" fill="currentColor" transform="rotate(-12 18.5 13.5)"/>
      <path d="M16.5 9.5l3 2.5 2.5-3" stroke="#444" stroke-width="1.2" fill="none" transform="rotate(-12 18.5 13.5)"/>
    </symbol>
    <symbol id="icon-account" viewBox="0 0 32 32">
      <ellipse cx="16" cy="10" rx="6.5" ry="7.5" fill="currentColor"/>
      <path d="M3 31c0-7 5-10.5 9-11.5l4 3 4-3c4 1 9 4.5 9 11.5z" fill="currentColor"/>
    </symbol>
  </defs>
</svg>

<!-- Promotions screen -->
<section class="screen screen--promotions">
  <div class="status-bar">
    <svg width="24" height="11" viewBox="0 0 24 11" aria-hidden="true"><g fill="#fff"><rect x="0" y="7" width="3" height="4"/><rect x="5" y="5" width="3" height="6"/><rect x="10" y="3" width="3" height="8"/><rect x="15" y="1" width="3" height="10"/><rect x="20" y="0" width="3" height="11"/></g></svg>
    <span class="status-time">8:08 PM</span>
    <svg width="26" height="12" viewBox="0 0 26 12" aria-hidden="true"><rect x="0.5" y="0.5" width="22" height="11" rx="2" fill="none" stroke="#fff"/><rect x="2.5" y="2.5" width="18" height="7" fill="#fff"/><rect x="23" y="4" width="2.5" height="4" fill="#fff"/></svg>
  </div>
  <header class="app-header">
    <div class="header-btn"><svg width="20" height="16" viewBox="0 0 20 16" aria-hidden="true"><path d="M1 2h18M1 8h18M1 14h18" stroke="#fff" stroke-width="2.4"/></svg></div>
    <h1 class="header-title">Promotions</h1>
    <div class="header-btn"><svg width="20" height="20" viewBox="0 0 20 20" aria-hidden="true"><circle cx="8" cy="8" r="6" stroke="#fff" stroke-width="2.4" fill="none"/><path d="M12.5 12.5l6 6" stroke="#fff" stroke-width="3" stroke-linecap="round"/></svg></div>
  </header>
  <div class="product-head">
    <span class="product-name">Organic Fruity Mocca Cake</span>
    <span class="product-price">$20</span>
  </div>
  <div class="product-photo" role="img" aria-label="Photo of a chocolate cake topped with cream, orange, strawberry and kiwi slices">
    <p class="product-caption">This organic cake created with mocca and fresh fruits inside, tasty and healthy. The promotion for the price discount and few bonus, so buy it now!</p>
  </div>
  <div class="offer-row">
    <div><div class="offer-name">Single: $20</div><div class="offer-qty">Order quantity : 2</div></div>
    <div class="basket-btn"><svg width="18" height="16" viewBox="0 0 32 30" style="color:#fff" aria-hidden="true"><use href="#icon-basket"/></svg>Add to basket</div>
  </div>
  <div class="offer-row">
    <div><div class="offer-name">Case: $35</div><div class="offer-qty">Order quantity : 3</div></div>
    <div class="basket-btn"><svg width="18" height="16" viewBox="0 0 32 30" style="color:#fff" aria-hidden="true"><use href="#icon-basket"/></svg>Add to basket</div>
  </div>
  <nav class="tab-bar">
    <div class="tab tab--active"><svg width="32" height="32" style="color:#e8f2fb" aria-label="Promotions"><use href="#icon-promotions"/></svg></div>
    <div class="tab"><svg width="30" height="30" style="color:var(--icon-light)" aria-label="Catalogue"><use href="#icon-catalogue"/></svg></div>
    <div class="tab"><svg width="32" height="32" style="color:var(--icon-light)" aria-label="Basket"><use href="#icon-basket"/></svg></div>
    <div class="tab"><svg width="30" height="30" style="color:var(--icon-light)" aria-label="Template"><use href="#icon-template"/></svg></div>
    <div class="tab"><svg width="32" height="32" style="color:var(--icon-light)" aria-label="Open order"><use href="#icon-open-order"/></svg></div>
    <div class="tab"><svg width="30" height="30" style="color:var(--icon-light)" aria-label="Account"><use href="#icon-account"/></svg></div>
  </nav>
</section>

<!-- Sign-in screen -->
<section class="screen screen--login">
  <div class="status-bar">
    <svg width="24" height="11" viewBox="0 0 24 11" aria-hidden="true"><g fill="#fff"><rect x="0" y="7" width="3" height="4"/><rect x="5" y="5" width="3" height="6"/><rect x="10" y="3" width="3" height="8"/><rect x="15" y="1" width="3" height="10"/><rect x="20" y="0" width="3" height="11"/></g></svg>
    <span class="status-time">8:08 PM</span>
    <svg width="26" height="12" viewBox="0 0 26 12" aria-hidden="true"><rect x="0.5" y="0.5" width="22" height="11" rx="2" fill="none" stroke="#fff"/><rect x="2.5" y="2.5" width="18" height="7" fill="#fff"/><rect x="23" y="4" width="2.5" height="4" fill="#fff"/></svg>
  </div>
  <div class="logo-badge">LOGO</div>
  <form class="login-form">
    <div class="field-group">
      <div class="field field--filled"><span>Kestrel<span class="caret"></span></span>
        <svg width="18" height="18" viewBox="0 0 32 32" style="color:#c4c4c4" aria-hidden="true"><use href="#icon-account"/></svg></div>
      <div class="field field--empty"><span>Password</span>
        <svg width="16" height="19" viewBox="0 0 16 19" aria-hidden="true"><path d="M4 8V5.5a4 4 0 0 1 8 0V8" stroke="#c4c4c4" stroke-width="2" fill="none"/><rect x="1.5" y="8" width="13" height="10" rx="1.5" fill="#c4c4c4"/><rect x="7" y="11" width="2" height="4" fill="#fff"/></svg></div>
    </div>
    <div class="signin-btn">Sign in</div>
    <p class="forgot-link">Forgotten password?</p>
  </form>
</section>

<!-- Home screen -->
<section class="screen screen--home">
  <div class="status-bar">
    <svg width="24" height="11" viewBox="0 0 24 11" aria-hidden="true"><g fill="#fff"><rect x="0" y="7" width="3" height="4"/><rect x="5" y="5" width="3" height="6"/><rect x="10" y="3" width="3" height="8"/><rect x="15" y="1" width="3" height="10"/><rect x="20" y="0" width="3" height="11"/></g></svg>
    <span class="status-time">8:08 PM</span>
    <svg width="26" height="12" viewBox="0 0 26 12" aria-hidden="true"><rect x="0.5" y="0.5" width="22" height="11" rx="2" fill="none" stroke="#fff"/><rect x="2.5" y="2.5" width="18" height="7" fill="#fff"/><rect x="23" y="4" width="2.5" height="4" fill="#fff"/></svg>
  </div>
  <header class="app-header">
    <div class="header-btn"><svg width="20" height="16" viewBox="0 0 20 16" aria-hidden="true"><path d="M1 2h18M1 8h18M1 14h18" stroke="#fff" stroke-width="2.4"/></svg></div>
    <h1 class="header-title">eShopping</h1>
    <div class="header-btn"><svg width="20" height="20" viewBox="0 0 20 20" aria-hidden="true"><path d="M9 2H2v16h16v-7" stroke="#fff" stroke-width="2" fill="none"/><path d="M8 12l1-3 8-8 2 2-8 8z" fill="#fff"/></svg></div>
  </header>
  <div class="welcome">
    <div class="logo-badge">LOGO</div>
    <p class="welcome-name">Hi, John Doe</p>
    <p class="welcome-text">Lorem ipsum dolor sit amet, consectetuer adipiscing elit. Aenean commodo ligula eget dolor. Aenean massa. Cum sociis natoque penatibus et magnis dis parturient</p>
  </div>
  <nav class="menu-grid">
    <div class="menu-tile"><svg width="50" height="50" style="color:var(--icon-light)" aria-hidden="true"><use href="#icon-promotions"/></svg>PROMOTIONS</div>
    <div class="menu-tile"><svg width="48" height="50" style="color:var(--icon-light)" aria-hidden="true"><use href="#icon-catalogue"/></svg>CATALOGUE</div>
    <div class="menu-tile menu-tile--active"><svg width="54" height="50" style="color:#e8f2fb" aria-hidden="true"><use href="#icon-basket"/></svg>BASKET</div>
    <div class="menu-tile"><svg width="48" height="52" style="color:var(--icon-light)" aria-hidden="true"><use href="#icon-template"/></svg>TEMPLATE</div>
    <div class="menu-tile"><svg width="50" height="50" style="color:var(--icon-light)" aria-hidden="true"><use href="#icon-open-order"/></svg>OPEN ORDER</div>
    <div class="menu-tile"><svg width="50" height="52" style="color:var(--icon-light)" aria-hidden="true"><use href="#icon-account"/></svg>ACCOUNT</div>
  </nav>
</section>

</body>
</html>
```